Boutique Wealth management firm needs a new business card design

I want to update my business card design to be more consistent with the look and feel of my website (www.corvalen-capital.example). I would like to incorporate an ivory parchment background and am open to switching from the current "portrait" layout to a more traditional "landscape" orientation. The final design should convey stability and exclusivity and I want something in PDF format that is ready to send to the printer
Updates

Thank you all for taking the time to submit your designs for my project. I've made my decision and picked the design I like best. Thanks again!

Industry/Entity Type

Business

```html
<!DOCTYPE html>
<html lang="en">
<head>
<meta charset="utf-8">
<title>Corvalen Capital – Business Card</title>
<link rel="stylesheet" href="https://fonts.googleapis.com/css2?family=Arimo:wght@400;700&display=swap">
<style>
  :root {
    --backdrop: #2f3a35;
    --parchment-light: #f1dd9c;
    --parchment-mid: #e6c978;
    --parchment-dark: #d6b35a;
    --maroon: #6e1024;
    --band: #2c0c16;
    --ink: #1f2a1c;
    --olive: #5a5a22;
    --cream-text: #f3ead6;
    --gold-rule: #d9b75c;
  }
  * { margin: 0; padding: 0; box-sizing: border-box; }
  html, body {
    width: 1200px; height: 1000px; overflow: hidden;
    background: var(--backdrop);
    font-family: "Arimo", Arial, sans-serif;
  }
  .stage {
    width: 1200px; height: 1000px;
    display: flex; align-items: center; justify-content: center;
  }
  .card {
    position: relative;
    width: 1050px; height: 600px;
    background: linear-gradient(135deg, var(--parchment-light) 0%, var(--parchment-mid) 55%, var(--parchment-dark) 100%);
    overflow: hidden;
  }
  .brand {
    position: absolute; top: 96px; left: 0; right: 0;
    text-align: center; padding-left: 180px;
    font-weight: 700; font-size: 64px; letter-spacing: 1px;
    color: var(--maroon);
  }
  .holder {
    position: absolute; top: 214px; left: 0; right: 0;
    text-align: center; padding-left: 80px;
  }
  .holder-name { font-weight: 700; font-size: 40px; color: var(--ink); }
  .holder-title { margin-top: 8px; font-weight: 700; font-size: 24px; color: var(--olive); }
  .contact-band {
    position: absolute; left: 0; right: 0; top: 338px; height: 170px;
    background: var(--band);
    display: flex; align-items: center;
    color: var(--cream-text); font-size: 26px; line-height: 1.3;
  }
  .mailing { width: 480px; text-align: right; padding-right: 36px; }
  .band-divider { width: 3px; height: 120px; background: var(--gold-rule); }
  .reach { padding-left: 40px; }
  .license {
    position: absolute; left: 150px; top: 528px;
    font-size: 26px; color: var(--ink);
  }
</style>
</head>
<body>
  <main class="stage">
    <section class="card" aria-label="Business card">
      <div class="brand">Corvalen Capital</div>
      <div class="holder">
        <div class="holder-name">Dale Harwick, CFP®</div>
        <div class="holder-title">Principal</div>
      </div>
      <div class="contact-band">
        <address class="mailing" style="font-style:normal">
          Mailing Address:<br>
          2870 Alder Ridge Rd. #214<br>
          Fairbrook, CA 95012
        </address>
        <div class="band-divider"></div>
        <div class="reach">
          555-014-2870<br>
          dale@corvalen-capital.example<br>
          www.corvalen-capital.example
        </div>
      </div>
      <div class="license">CA Insurance License #0K71836</div>
    </section>
  </main>
</body>
</html>
```